Power Point Digital Signage Template Needed

The North Calloway Health Centre and Pharmacy (ourcalloway.example) needs a power point digital signage template that is customizable and pulls pertinent local information like weather, news and generic health tips. Please use design and colors from art work and website. We would need the power point project to be able to be read clearly at a distance of around 10 - 15 feet and provide the viewer with all information about our clinic/pharmacy services while attracting their attention with local news or weather reports and health tips.

Target Market(s)

People in waiting room, healthcare , family doctor patients to drive pharmacy business and healthcare centre awareness

Industry/Entity Type

Healthcare

Font styles to use
Serif
Sans Serif

Colors

Designer to choose colors to be used in the design.

Requirements
Must have
• Links to real time local weather
• Scrolling News
• Scrolling Health tips
• Fully Customizable
• Power Point Format
• Multiple Slides for each feature (example 1 for real time weather, 1 slide for news, 1 slide for cliinic hours etc)
• At least 20 customizable slides on contiual rotation

```html
<!DOCTYPE html>
<html lang="en">
<head>
<meta charset="utf-8">
<title>North Calloway Health Centre and Pharmacy – Weather Forecast</title>
<link rel="stylesheet" href="https://fonts.googleapis.com/css2?family=Montserrat:wght@600;700&family=Arimo:wght@400;700&display=swap">
<style>
:root{
  --sky-top:#b9d3ea;
  --sky-mid:#e4eef6;
  --haze:#eef3f3;
  --grass:#8fae55;
  --grass-deep:#5f7e34;
  --brand-green:#1f8a4c;
  --band-dark:#373737;
  --white:#ffffff;
  --ink:#1a1a1a;
  --ink-soft:#555;
  --link:#1b6fa8;
  --accent-blue:#4fb5e5;
  --head-blue:#dcedf7;
  --row-line:#cfe1ec;
  --temp-warm:#d4202a;
  --temp-cold:#1a8dd0;
  --sun:#f5b50f;
  --cloud:#d9dde1;
  --map-land:#eceeec;
  --map-water:#cfd3d3;
}
*{box-sizing:border-box;margin:0;padding:0}
html,body{width:1200px;height:678px;overflow:hidden;background:var(--white)}
.slide{position:relative;width:1200px;height:678px;overflow:hidden;font-family:"Arimo",Arial,sans-serif;color:var(--ink)}
.backdrop{position:absolute;inset:0;background:linear-gradient(180deg,var(--sky-top) 0%,var(--sky-mid) 35%,var(--haze) 62%,var(--grass) 80%,var(--grass-deep) 100%)}
.runners{position:absolute;left:70px;top:455px;width:340px;height:200px;border-radius:40px;background:radial-gradient(ellipse at center,rgba(70,80,90,.35),rgba(70,80,90,0) 70%)}

.brand{position:absolute;left:100px;top:150px;width:260px;text-align:center;font-family:"Montserrat",Arial,sans-serif;font-weight:600;color:var(--brand-green)}
.brand-dot{width:70px;height:70px;border-radius:50%;background:var(--brand-green);margin:0 auto 26px}
.brand-name{font-size:27px;line-height:1.05}
.brand-sub{font-size:10px;letter-spacing:2px;margin-top:6px}

.title-band{position:absolute;left:431px;top:27px;width:75px;height:336px;background:var(--band-dark)}
.title-band h1{position:absolute;left:50%;top:50%;transform:translate(-50%,-50%) rotate(-90deg);white-space:nowrap;font-family:"Montserrat",Arial,sans-serif;font-weight:700;font-size:30px;color:var(--white)}

.site{position:absolute;left:506px;top:27px;width:673px;height:627px;background:var(--white)}
.scrollbar{position:absolute;left:1169px;top:27px;width:10px;height:627px;background:#f0f0f0}
.scrollbar::after{content:"";position:absolute;left:2px;top:8px;width:6px;height:240px;background:#c4c4c4;border-radius:3px}
.abs{position:absolute}
.top-link{font-size:7px;color:var(--link)}
.site-mark{left:528px;top:55px;font-weight:700;font-size:10px;line-height:14px;color:var(--accent-blue);white-space:nowrap}
.search{left:572px;top:49px;width:227px;height:27px;border:1px solid #bbb;background:#f4f4f4;font-size:9px;color:#999;padding:8px 10px}
.search svg{position:absolute;right:8px;top:8px}
.nav-link{font-size:9px;color:var(--link)}
.crumbs{left:526px;top:86px;width:623px;height:16px;background:var(--head-blue);display:flex;font-size:7px;color:#333}
.crumbs span{padding:4px 12px 0 12px;position:relative}
.crumbs span+span{margin-left:16px}
.crumbs .current{color:#888}
.lead{left:526px;top:119px;font-size:11px}
.place{left:526px;top:131px;font-size:21px}
.place b{font-weight:700}
.updated{left:1006px;top:116px;font-size:6px;color:#555}
.updated b{color:#222}
.actions{left:1008px;top:134px;font-size:6.5px;color:var(--link);display:flex;gap:14px;align-items:center}
.pdf-box{display:inline-block;width:13px;height:16px;border:1px solid #c33;background:#fbe9e9;vertical-align:middle;margin-right:4px}
.rule{left:526px;top:156px;width:623px;height:1px;background:#ddd}

.side-nav{left:526px;top:166px;width:82px;font-size:7px;color:#333}
.side-nav li{list-style:none;height:18px;padding:4px 0 0 4px;display:flex;gap:5px;align-items:center}
.side-nav li.active{background:var(--head-blue);font-weight:700;color:#123}
.side-nav li i{display:inline-block;width:7px;height:7px;border:1px solid #333;border-radius:1px}
.side-divider{left:608px;top:166px;width:1px;height:488px;background:#ddd}
.side-heading{left:526px;top:278px;font-size:7px;letter-spacing:.3px;color:#333}
.side-place{left:526px;top:297px;font-size:7px;color:var(--link);text-decoration:underline}
.side-hint{left:528px;top:327px;font-size:6px;color:#444;line-height:1.3;display:flex;gap:6px}

.day-title{left:628px;font-size:9.5px}
.day-title b{font-weight:700}
.forecast{position:absolute;left:628px;width:301px;border-collapse:collapse;font-size:6.3px;color:#333}
.forecast th{height:14px;background:var(--head-blue);border-top:2px solid var(--accent-blue);font-weight:400;border-left:1px solid #fff}
.forecast td{height:30px;border-bottom:1px solid var(--row-line);text-align:center;vertical-align:middle}
.forecast td.wind{text-align:left;padding-left:6px}
.wind-cell{display:flex;align-items:center;gap:10px;line-height:1.3}
.wind-cell svg{flex:none}
.forecast .c-time{width:37px;line-height:1.4}
.forecast .c-icon{width:37px}
.forecast .c-temp{width:28px;font-size:8.5px;font-weight:700}
.forecast .c-rain{width:52px}
.warm{color:var(--temp-warm)}
.cold{color:var(--temp-cold)}
.note{left:628px;top:629px;font-size:6.8px;font-weight:700}
.webcams{left:628px;top:641px;font-size:9px}
.webcams b{font-weight:700}

.map{left:948px;top:185px;width:200px;height:293px;border:1px solid var(--accent-blue);border-top:2px solid var(--accent-blue);background:linear-gradient(160deg,var(--map-water) 0%,var(--map-land) 35%,var(--map-land) 100%)}
.map-bar{left:948px;top:466px;width:200px;height:12px;font-size:6.5px;font-weight:700;display:flex;justify-content:space-between;align-items:center;padding:0 14px 0 4px}
.map-bar i{display:block;width:12px;height:8px;border:1px solid #222;border-radius:2px}
.sun-title{left:948px;top:500px;font-size:9.5px}
.sun-title b{font-weight:700}
.sun-table{position:absolute;left:948px;top:513px;width:200px;border-collapse:collapse;font-size:6.3px;color:#333}
.sun-table th{height:12px;background:var(--head-blue);border-top:2px solid var(--accent-blue);font-weight:400}
.sun-table td{height:15px;border-bottom:1px solid var(--row-line);padding-left:4px}
.sun-table td.icon{width:30px;text-align:center;padding:0}
</style>
</head>
<body>
<svg width="0" height="0" style="position:absolute">
  <defs>
    <symbol id="icon-sun" viewBox="0 0 24 24"><g stroke="#f5b50f" stroke-width="2"><line x1="12" y1="1" x2="12" y2="5"/><line x1="12" y1="19" x2="12" y2="23"/><line x1="1" y1="12" x2="5" y2="12"/><line x1="19" y1="12" x2="23" y2="12"/><line x1="4" y1="4" x2="7" y2="7"/><line x1="17" y1="17" x2="20" y2="20"/><line x1="4" y1="20" x2="7" y2="17"/><line x1="17" y1="7" x2="20" y2="4"/></g><circle cx="12" cy="12" r="6" fill="#f5b50f"/></symbol>
    <symbol id="icon-partly" viewBox="0 0 24 24"><circle cx="9" cy="9" r="5" fill="#f5b50f"/><ellipse cx="14" cy="15" rx="9" ry="5" fill="#d9dde1"/></symbol>
    <symbol id="icon-cloud" viewBox="0 0 24 24"><ellipse cx="12" cy="13" rx="10" ry="5.5" fill="#d9dde1"/></symbol>
    <symbol id="icon-moon-cloud" viewBox="0 0 24 24"><path d="M8 3a6 6 0 1 0 6 8 5 5 0 0 1-6-8z" fill="#555"/><ellipse cx="14" cy="15" rx="9" ry="5" fill="#d9dde1"/></symbol>
    <symbol id="icon-moon" viewBox="0 0 24 24"><path d="M11 4a8 8 0 1 0 8 10 7 7 0 0 1-8-10z" fill="#555"/></symbol>
    <symbol id="icon-arrow" viewBox="0 0 12 24"><line x1="6" y1="3" x2="6" y2="20" stroke="#222" stroke-width="1.4"/><path d="M3 17l3 5 3-5z" fill="#222"/></symbol>
  </defs>
</svg>

<main class="slide">
  <div class="backdrop" role="img" aria-label="Photo backdrop: pale sky over a green hillside meadow"></div>
  <div class="runners" role="img" aria-label="Photo: four adults jogging together across the meadow"></div>

  <div class="brand">
    <div class="brand-dot"></div>
    <div class="brand-name">North Calloway</div>
    <div class="brand-sub">Health Centre + Pharmacy</div>
  </div>

  <div class="title-band"><h1>Weather Forecast</h1></div>

  <section class="site" aria-label="Weather forecast web page"></section>
  <div class="scrollbar"></div>

  <span class="abs top-link" style="left:992px;top:31px">Mobile version</span>
  <span class="abs top-link" style="left:1070px;top:31px">Språk / Language ▾</span>
  <div class="abs site-mark">SkyCast</div>
  <div class="abs search">Search for a location…
    <svg width="10" height="10" viewBox="0 0 10 10"><circle cx="4" cy="4" r="3" fill="none" stroke="#333" stroke-width="1.2"/><line x1="6.3" y1="6.3" x2="9.5" y2="9.5" stroke="#333" stroke-width="1.2"/></svg>
  </div>
  <span class="abs nav-link" style="left:810px;top:57px">Advanced search</span>
  <span class="abs nav-link" style="left:1088px;top:57px;color:#333">☆ My places</span>

  <nav class="abs crumbs">
    <span>Front page</span><span>Canada</span><span>Manitoba</span><span class="current">Winnipeg</span>
  </nav>

  <div class="abs lead">Weather forecast for</div>
  <div class="abs place"><b>Winnipeg</b>, Manitoba (Canada)</div>
  <div class="abs updated">Updated at 2:37. &nbsp;<b>Next update around 15:00.</b></div>
  <div class="abs actions"><span>★ Add to My places</span><span><i class="pdf-box"></i>Forecast as PDF</span></div>
  <div class="abs rule"></div>

  <ul class="abs side-nav">
    <li class="active"><i></i>Overview</li>
    <li><i style="border-radius:50%"></i>Hour by hour</li>
    <li><i></i>Long term</li>
    <li><i></i>Statistics</li>
    <li style="margin-top:6px"><i></i>Maps</li>
  </ul>
  <div class="abs side-divider"></div>
  <div class="abs side-heading">RELEVANT PLACES</div>
  <div class="abs side-place">Winnipeg</div>
  <div class="abs side-hint"><span style="color:var(--accent-blue)">↓</span><span>To the main menu at<br>the page bottom</span></div>

  <div class="abs day-title" style="top:171px"><b>Today,</b> Thursday 10/05/2018</div>
  <table class="forecast" style="top:186px">
    <thead><tr><th class="c-time">Time</th><th class="c-icon">Forecast</th><th class="c-temp" style="font-size:6.3px;font-weight:400">Temp.</th><th class="c-rain">Precipitation</th><th>Wind</th></tr></thead>
    <tbody>
      <tr><td class="c-time">08:00–<br>12:00</td><td><svg width="22" height="22"><use href="#icon-partly"/></svg></td><td class="c-temp warm">4°</td><td>0 mm</td><td class="wind"><div class="wind-cell"><svg width="8" height="16" style="transform:rotate(-23deg)"><use href="#icon-arrow"/></svg>Gentle breeze, 5 m/s from north-<br>northwest</div></td></tr>
      <tr><td class="c-time">12:00–<br>18:00</td><td><svg width="22" height="22"><use href="#icon-partly"/></svg></td><td class="c-temp warm">8°</td><td>0 mm</td><td class="wind"><div class="wind-cell"><svg width="8" height="16"><use href="#icon-arrow"/></svg>Gentle breeze, 4 m/s from north</div></td></tr>
      <tr><td class="c-time">18:00–<br>00:00</td><td><svg width="22" height="22"><use href="#icon-partly"/></svg></td><td class="c-temp warm">12°</td><td>0 mm</td><td class="wind"><div class="wind-cell"><svg width="8" height="16"><use href="#icon-arrow"/></svg>Light breeze, 3 m/s from north</div></td></tr>
    </tbody>
  </table>

  <div class="abs day-title" style="top:304px"><b>Tomorrow,</b> Friday 11/05/2018</div>
  <table class="forecast" style="top:319px">
    <thead><tr><th class="c-time">Time</th><th class="c-icon">Forecast</th><th class="c-temp" style="font-size:6.3px;font-weight:400">Temp.</th><th class="c-rain">Precipitation</th><th>Wind</th></tr></thead>
    <tbody>
      <tr><td class="c-time">00:00–<br>06:00</td><td><svg width="22" height="22"><use href="#icon-moon-cloud"/></svg></td><td class="c-temp warm">2°</td><td>0 mm</td><td class="wind"><div class="wind-cell"><svg width="8" height="16" style="transform:rotate(90deg)"><use href="#icon-arrow"/></svg>Light breeze, 2 m/s from east</div></td></tr>
      <tr><td class="c-time">06:00–<br>12:00</td><td><svg width="22" height="22"><use href="#icon-cloud"/></svg></td><td class="c-temp cold">-1°</td><td>0 mm</td><td class="wind"><div class="wind-cell"><svg width="8" height="16" style="transform:rotate(68deg)"><use href="#icon-arrow"/></svg>Light breeze, 2 m/s from east-<br>southeast</div></td></tr>
      <tr><td class="c-time">12:00–<br>18:00</td><td><svg width="22" height="22"><use href="#icon-cloud"/></svg></td><td class="c-temp warm">12°</td><td>0 mm</td><td class="wind"><div class="wind-cell"><svg width="8" height="16" style="transform:rotate(90deg)"><use href="#icon-arrow"/></svg>Light air, 1 m/s from east</div></td></tr>
      <tr><td class="c-time">18:00–<br>00:00</td><td><svg width="22" height="22"><use href="#icon-partly"/></svg></td><td class="c-temp warm">14°</td><td>0 mm</td><td class="wind"><div class="wind-cell"><svg width="8" height="16" style="transform:rotate(20deg)"><use href="#icon-arrow"/></svg>Light air, 1 m/s from north-northeast</div></td></tr>
    </tbody>
  </table>

  <div class="abs day-title" style="top:467px"><b>Saturday,</b> 12/05/2018</div>
  <table class="forecast" style="top:482px">
    <thead><tr><th class="c-time">Time</th><th class="c-icon">Forecast</th><th class="c-temp" style="font-size:6.3px;font-weight:400">Temp.</th><th class="c-rain">Precipitation</th><th>Wind</th></tr></thead>
    <tbody>
      <tr><td class="c-time">00:00–<br>06:00</td><td><svg width="18" height="18"><use href="#icon-moon"/></svg></td><td class="c-temp warm">6°</td><td>0 mm</td><td class="wind"><div class="wind-cell"><svg width="8" height="16" style="transform:rotate(225deg)"><use href="#icon-arrow"/></svg>Light breeze, 2 m/s from southwest</div></td></tr>
      <tr><td class="c-time">06:00–<br>12:00</td><td><svg width="20" height="20"><use href="#icon-sun"/></svg></td><td class="c-temp warm">3°</td><td>0 mm</td><td class="wind"><div class="wind-cell"><svg width="8" height="16" style="transform:rotate(225deg)"><use href="#icon-arrow"/></svg>Light breeze, 2 m/s from southwest</div></td></tr>
      <tr><td class="c-time">12:00–<br>18:00</td><td><svg width="20" height="20"><use href="#icon-sun"/></svg></td><td class="c-temp warm">18°</td><td>0 mm</td><td class="wind"><div class="wind-cell"><svg width="8" height="16" style="transform:rotate(247deg)"><use href="#icon-arrow"/></svg>Gentle breeze, 4 m/s from west-<br>southwest</div></td></tr>
      <tr><td class="c-time">18:00–<br>00:00</td><td><svg width="20" height="20"><use href="#icon-sun"/></svg></td><td class="c-temp warm">21°</td><td>0 mm</td><td class="wind"><div class="wind-cell"><svg width="8" height="16" style="transform:rotate(255deg)"><use href="#icon-arrow"/></svg>Gentle breeze, 4 m/s from west-<br>southwest</div></td></tr>
    </tbody>
  </table>

  <div class="abs note">The forecast shows local time for Winnipeg.</div>
  <div class="abs webcams"><b>Webcams</b> close to Winnipeg</div>

  <div class="abs map" role="img" aria-label="Regional map of southern Manitoba centred on Winnipeg with a sunny weather marker"></div>
  <div class="abs map-bar"><i></i><span>today at 10</span></div>

  <div class="abs sun-title"><b>Sun and moon,</b> 10/05/2018</div>
  <table class="sun-table">
    <thead><tr><th colspan="2">Sun</th><th colspan="2">Moon</th></tr></thead>
    <tbody>
      <tr><td class="icon" rowspan="2"><svg width="18" height="18"><use href="#icon-sun"/></svg></td><td>Sunrise 05:50</td><td class="icon" rowspan="2"><svg width="16" height="16"><use href="#icon-moon"/></svg></td><td>Moonrise 04:08</td></tr>
      <tr><td>Sunset 21:00</td><td>Moonset 15:15</td></tr>
    </tbody>
  </table>
</main>
</body>
</html>
```